We need a business card for a company which is just starting up. The company name is Meridale Executive Services and we do a variety of things such as: support services for executives/leaders, sales team creation/management/training, and implementation of new programs to enhance a company's culture. The final design should be simple, professional and create a buzz of wanting to learn more. The owner is a woman of power, poise and leadership while she maintains qualities of caring, compassionate and honest. Her clients respect and refer her constantly. The colors are up for negotiation but should capture strength and softness at the same time. Possible colors: chocolate brown, dark pink, periwinkle. See attachment.

Target Market(s)

Medium to Large Businesses

Industry/Entity Type

Leadership

Requirements
Nice to have
• Qr code

```html
<!DOCTYPE html>
<html lang="en">
<head>
<meta charset="utf-8">
<title>Meridale Executive Services – Business Card</title>
<link rel="stylesheet" href="https://fonts.googleapis.com/css2?family=Cabin:wght@400;600&display=swap">
<style>
  :root {
    --cocoa: #514841;
    --cocoa-deep: #372e2b;
    --pink-deep: #bf2e69;
    --pink-bright: #ff62a2;
    --pink-rule: #f062a0;
    --sand: #c9b5a1;
    --taupe: #91857a;
    --ink-plum: #3b2730;
  }
  html, body {
    margin: 0;
    padding: 0;
    overflow: hidden;
  }
  body {
    width: 1200px;
    height: 800px;
    background: var(--cocoa);
  }
  .card {
    position: relative;
    width: 1200px;
    height: 800px;
    background: var(--cocoa);
    font-family: "Cabin", "Trebuchet MS", sans-serif;
    overflow: hidden;
  }
  .top-band {
    position: absolute;
    left: 0; top: 0;
    width: 100%;
    height: 59px;
    background: linear-gradient(to bottom, var(--pink-deep) 0%, #d8407c 45%, var(--pink-bright) 100%);
  }
  .company-name {
    position: absolute;
    top: 120px;
    left: 0;
    width: 100%;
    margin: 0;
    text-align: center;
    font-size: 48px;
    font-weight: 600;
    color: var(--sand);
    letter-spacing: 0.3px;
  }
  .title-rule {
    position: absolute;
    left: 427px;
    top: 226px;
    width: 346px;
    height: 3px;
    background: var(--pink-rule);
    box-shadow: 0 1px 1px rgba(0,0,0,0.35);
  }
  .contact-box {
    position: absolute;
    left: 369px;
    top: 304px;
    width: 468px;
    height: 200px;
    box-sizing: border-box;
    padding: 12px 0 0 23px;
    background: var(--pink-deep);
    box-shadow: 2px 3px 3px rgba(0,0,0,0.55);
    color: var(--ink-plum);
    font-size: 35px;
    line-height: 42px;
  }
  .contact-box p { margin: 0; white-space: nowrap; }
  .website {
    position: absolute;
    top: 612px;
    left: 0;
    width: 100%;
    margin: 0;
    text-align: center;
    font-size: 29px;
    color: var(--taupe);
  }
  .petal-band {
    position: absolute;
    left: 0;
    top: 680px;
    width: 100%;
    height: 120px;
    background: linear-gradient(to bottom, var(--cocoa-deep) 0%, #5a3544 55%, #6e3a52 100%);
  }
</style>
</head>
<body>
  <div class="card">
    <div class="top-band"></div>

    <h1 class="company-name">Meridale Executive Services</h1>
    <div class="title-rule"></div>

    <div class="contact-box">
      <p>Renata Vallis, Owner</p>
      <p>555 W. 5th St.</p>
      <p>Phone (555) 555-5555</p>
      <p>Email renata@email.com</p>
    </div>

    <p class="website">Visit our Website: www.website.com</p>

    <div class="petal-band" role="img" aria-label="Scattered pink, white and taupe leaf petals over a dark brown band"></div>
  </div>
</body>
</html>
```